Riverbend Haven Home Care-Nursing Assessment Form

I am creating a Nursing Assessment Form (which is used to be an intake form for all new patients) for my new home care company, Riverbend Haven Home Care.

It is 15 pages and pretty comprehensive as this is a very regulated field. I have all the necessary content and information attached in the word document below. Now, I am seeking a designer to make it look professional, cohesive and easy to read/ follow.
In order for your Word Document Design to be selected, you must:

1. As mentioned previously, make it easy to read/follow. There should be enough spacing, room to write out all necessary notes, fill out check marks...etc...
2. It should look professional.
3. It should be attractive and eye pleasing. Attached you will find our logo-kindly incorporate it's style into the project as well. The logo should be placed on top of each page.
4. Lastly, we need a Word Document version AND PDF Fillable Option. The fillable PDF should Auto Fill for the Name and Start of Care (SOC) Date.

I have attached a sample form below as well. This is how I envision the finished project to look. Of course, I am open to other suggestions as look as it meets the aforementioned requirements.

Thank you! May the best man or woman win!
Our team looks forward to working with our designer on this project!

Industry/Entity Type

Home Health Care

Font styles to use
Sans Serif

Colors
0255a3
9bcb3c

Requirements
Must have
• Refer to Project Description above.
Nice to have
We must be given a Word Document Option and PDF Fillable Option.

```html
<!DOCTYPE html>
<html lang="en">
<head>
<meta charset="utf-8">
<title>Riverbend Haven Home Care – Initial Assessment Form</title>
<link rel="stylesheet" href="https://fonts.googleapis.com/css2?family=Mulish:wght@700;800&family=Roboto+Condensed:wght@400;700&display=swap">
<style>
:root{
  --brand-blue:#0255a3;
  --brand-green:#9bcb3c;
  --heading-blue:#0b3f94;
  --panel-blue:#a9e1f8;
  --field-green:#d7f0c4;
  --ink:#111;
  --backdrop:#e6eaef;
  --paper:#fff;
}
*{box-sizing:border-box;margin:0;padding:0}
html,body{width:1200px;height:731px;overflow:hidden;background:var(--backdrop)}
.sheet{position:absolute;left:324px;top:8px;width:1110px;height:1437px;background:var(--paper);
  transform:scale(.4976);transform-origin:0 0;box-shadow:0 0 12px rgba(0,0,0,.25);
  font-family:'Roboto Condensed',sans-serif;color:var(--ink)}
.header-band{position:absolute;left:0;top:0;width:1110px;height:116px}
.brand-name{position:absolute;left:52px;top:88px;display:flex;align-items:center;gap:10px;
  font:800 17px/1.1 'Mulish',sans-serif;color:var(--brand-blue);width:200px}
.brand-name i{display:block;flex:none;width:26px;height:26px;border-radius:50%;background:var(--brand-green)}
.company-tag{position:absolute;left:338px;top:29px;width:372px;height:27px;background:var(--brand-green);
  color:#fff;font:700 21px/27px 'Mulish',sans-serif;text-align:center;letter-spacing:.3px}
.form-title{position:absolute;left:334px;top:52px;color:#fff;font:800 54px/1 'Mulish',sans-serif;letter-spacing:-.5px}
.t{position:absolute;font-size:15px;line-height:18px;white-space:nowrap;transform:translateY(-50%)}
.b{font-weight:700}
.h{position:absolute;font:800 16px/18px 'Mulish',sans-serif;color:var(--heading-blue);transform:translateY(-50%);letter-spacing:.3px}
.u{text-decoration:underline}
.f{position:absolute;height:19px;background:var(--field-green);transform:translateY(-50%)}
.w{background:#fff}
.c{position:absolute;width:18px;height:18px;background:var(--field-green);transform:translateY(-50%)}
.patient-panel{position:absolute;left:51px;top:160px;width:1010px;height:125px;background:var(--panel-blue)}
.note-box{position:absolute;left:48px;top:1309px;width:1015px;height:57px;background:var(--field-green)}
</style>
</head>
<body>
<div class="sheet">
  <svg class="header-band" viewBox="0 0 1110 116" aria-hidden="true"><polygon points="258,0 1110,0 1110,116 285,116" fill="#0255a3"/></svg>
  <div class="brand-name"><i></i><span>RIVERBEND HAVEN HOME CARE</span></div>
  <div class="company-tag">RIVERBEND HAVEN HOME CARE</div>
  <div class="form-title">Initial Assessment Form</div>

  <span class="t b" style="left:337px;top:128px">Name :</span><div class="f" style="left:386px;top:128px;width:446px"></div>
  <span class="t b" style="left:839px;top:128px">SOC Date :</span><div class="f" style="left:913px;top:128px;width:146px"></div>

  <div class="patient-panel"></div>
  <span class="t b" style="left:66px;top:189px">Patient’s Name</span><div class="f w" style="left:167px;top:189px;width:547px"></div>
  <span class="t b" style="left:718px;top:189px">Gender</span><div class="f w" style="left:768px;top:189px;width:72px"></div>
  <span class="t b" style="left:843px;top:189px">MR#</span><div class="f w" style="left:875px;top:189px;width:78px"></div>
  <span class="t b" style="left:957px;top:189px">Date</span><div class="f w" style="left:990px;top:189px;width:71px"></div>
  <span class="t b" style="left:66px;top:213px">Primary Diagnosis</span><div class="f w" style="left:188px;top:213px;width:389px"></div>
  <span class="t b" style="left:582px;top:213px">Secondary Diagnosis</span><div class="f w" style="left:725px;top:213px;width:336px"></div>
  <span class="t b" style="left:66px;top:237px">Other Pertinent Diagnosis</span><div class="f w" style="left:236px;top:237px;width:341px"></div>
  <span class="t b" style="left:582px;top:237px">PCP name</span><div class="f w" style="left:726px;top:237px;width:335px"></div>
  <span class="t b" style="left:66px;top:262px">Other Physician Name</span><div class="f w" style="left:211px;top:262px;width:366px"></div>

  <span class="t b" style="left:51px;top:302px">Prognosis:</span>
  <div class="c" style="left:145px;top:302px"></div><span class="t" style="left:167px;top:302px">Poor</span>
  <div class="c" style="left:245px;top:302px"></div><span class="t" style="left:266px;top:302px">Fair</span>
  <div class="c" style="left:327px;top:302px"></div><span class="t" style="left:349px;top:302px">Good</span>
  <div class="c" style="left:420px;top:302px"></div><span class="t" style="left:442px;top:302px">Excellent</span>

  <span class="t b" style="left:51px;top:326px">Vital Signs:</span>
  <span class="t" style="left:138px;top:326px">Height:</span><div class="f" style="left:181px;top:326px;width:54px"></div>
  <span class="t" style="left:243px;top:326px">Weight:</span><div class="f" style="left:289px;top:326px;width:88px"></div>
  <span class="t" style="left:386px;top:326px">Temp:</span><div class="f" style="left:428px;top:326px;width:75px"></div>
  <span class="t" style="left:519px;top:326px">Pulse:</span><div class="f" style="left:560px;top:326px;width:90px"></div>
  <span class="t" style="left:658px;top:326px">Resp:</span><div class="f" style="left:697px;top:326px;width:81px"></div>
  <span class="t" style="left:786px;top:326px">B/P:</span><div class="f" style="left:815px;top:326px;width:85px"></div>
  <span class="t b" style="left:51px;top:350px">Allergies:</span><div class="f" style="left:116px;top:350px;width:532px"></div>
  <span class="t b" style="left:51px;top:374px">Past Medical and Surgical History:</span><div class="f" style="left:275px;top:374px;width:784px"></div>

  <span class="h" style="left:51px;top:415px">SUPPORT SYSTEM :</span>
  <span class="t" style="left:51px;top:440px">Married/Not Married/Single/Divorced/Widowed</span>
  <span class="t" style="left:51px;top:464px">Lives Alone:</span>
  <div class="c" style="left:143px;top:464px"></div><span class="t" style="left:165px;top:464px">Yes</span>
  <div class="c" style="left:204px;top:464px"></div><span class="t" style="left:226px;top:464px">No</span>
  <span class="t" style="left:51px;top:488px">Family Composition:</span><div class="f" style="left:177px;top:488px;width:308px"></div>
  <span class="t" style="left:51px;top:512px">Legal Next of Kin:</span><div class="f" style="left:158px;top:512px;width:327px"></div>
  <span class="t" style="left:492px;top:512px">Telephone:</span><div class="f" style="left:564px;top:512px;width:245px"></div>
  <span class="t" style="left:817px;top:512px">/</span><div class="f" style="left:828px;top:512px;width:230px"></div>
  <span class="t" style="left:51px;top:536px">Address:</span><div class="f" style="left:109px;top:536px;width:376px"></div>
  <span class="t" style="left:492px;top:536px">E-mail&nbsp;&nbsp;&nbsp;&nbsp;:</span><div class="f" style="left:564px;top:536px;width:246px"></div>
  <span class="t" style="left:51px;top:560px">Is significant other able, available, capable and willing to care for patient?</span>
  <div class="c" style="left:565px;top:560px"></div><span class="t" style="left:590px;top:560px">Yes</span>
  <div class="c" style="left:644px;top:560px"></div><span class="t" style="left:669px;top:560px">No</span>
  <span class="t" style="left:51px;top:584px">If No, explain:</span><div class="f" style="left:137px;top:584px;width:920px"></div>
  <span class="t" style="left:51px;top:608px">Educational Needs of Patient/Family:</span><div class="f" style="left:275px;top:608px;width:782px"></div>

  <span class="h" style="left:51px;top:650px">ENVIRONMENT :</span>
  <div class="c" style="left:52px;top:674px"></div><span class="t" style="left:74px;top:674px">Private Home</span>
  <div class="c" style="left:232px;top:674px"></div><span class="t" style="left:254px;top:674px">Elevator</span>
  <div class="c" style="left:386px;top:674px"></div><span class="t" style="left:408px;top:674px">Apartment</span>
  <div class="c" style="left:553px;top:674px"></div><span class="t" style="left:575px;top:674px">Walkup</span>

  <span class="h" style="left:51px;top:715px">SAFETY HAZARDS IN THE HOME:</span>
  <div class="c" style="left:52px;top:740px"></div><span class="t" style="left:74px;top:740px">Sound structure</span>
  <div class="c" style="left:52px;top:764px"></div><span class="t" style="left:74px;top:764px">Adequate Cooking facility</span>
  <div class="c" style="left:52px;top:788px"></div><span class="t" style="left:74px;top:788px">Safe Gas/Electric Appliances</span>
  <div class="c" style="left:52px;top:812px"></div><span class="t" style="left:74px;top:812px">Working Telephone in the Home</span>
  <div class="c" style="left:52px;top:836px"></div><span class="t" style="left:74px;top:836px">Working smoke detectors?</span>
  <div class="c" style="left:52px;top:860px"></div><span class="t" style="left:74px;top:860px">Neighborhood safe?</span>
  <div class="c" style="left:386px;top:740px"></div><span class="t" style="left:408px;top:740px">Safe Placement of Cords, Rugs and Furniture</span>
  <div class="c" style="left:386px;top:764px"></div><span class="t" style="left:408px;top:764px">Adequate Plumbing/Sanitation/ Running Water</span>
  <div class="c" style="left:386px;top:788px"></div><span class="t" style="left:408px;top:788px">Grounded Plug for Equipment</span>
  <div class="c" style="left:386px;top:812px"></div><span class="t" style="left:408px;top:812px">Safe storage for Supplies/Equipment/Meds?</span>
  <div class="c" style="left:386px;top:836px"></div><span class="t" style="left:408px;top:836px">Fire extinguisher in home?</span>
  <div class="c" style="left:746px;top:740px"></div><span class="t" style="left:768px;top:740px">Adequate Heating and Ventilation</span>
  <div class="c" style="left:746px;top:764px"></div><span class="t" style="left:768px;top:764px">Adequate Sleeping Arrangement</span>
  <div class="c" style="left:746px;top:788px"></div><span class="t" style="left:768px;top:788px">Enough Electrical Outlets for Equipment</span>
  <div class="c" style="left:746px;top:812px"></div><span class="t" style="left:768px;top:812px">Exits Free of Obstruction</span>
  <div class="c" style="left:746px;top:836px"></div><span class="t" style="left:768px;top:836px">Infestations of pests?</span>
  <span class="t" style="left:51px;top:885px">Comments:</span><div class="f" style="left:121px;top:885px;width:937px"></div>

  <span class="h" style="left:51px;top:926px">CAREGIVER’S CONTACT INFORMATION:</span>
  <span class="t" style="left:51px;top:951px">Name</span><span class="t" style="left:193px;top:951px">:</span><div class="f" style="left:206px;top:951px;width:540px"></div>
  <span class="t" style="left:51px;top:975px">Telephone</span><span class="t" style="left:193px;top:975px">:</span><div class="f" style="left:206px;top:975px;width:182px"></div>
  <span class="t" style="left:389px;top:975px">/</span><div class="f" style="left:397px;top:975px;width:349px"></div>
  <span class="t" style="left:51px;top:999px">Address</span><span class="t" style="left:193px;top:999px">:</span><div class="f" style="left:206px;top:999px;width:275px"></div>
  <span class="t" style="left:485px;top:999px">E-mail:</span><div class="f" style="left:531px;top:999px;width:215px"></div>
  <span class="t" style="left:51px;top:1023px">Days / Time Available</span><span class="t" style="left:193px;top:1023px">:</span><div class="f" style="left:206px;top:1023px;width:541px"></div>

  <span class="h" style="left:51px;top:1064px">CAREGIVERS ABILITY TO ASSIST PATIENT / ABLE TO PROVIDE:</span>
  <span class="t" style="left:51px;top:1089px">Personal Care:</span>
  <span class="t" style="left:51px;top:1113px">Mobility:</span>
  <span class="t" style="left:51px;top:1137px">Prepare/Serve Meals:</span>
  <span class="t" style="left:51px;top:1161px">Maintain Safe/Clean Environment:</span>
  <span class="t" style="left:51px;top:1185px">Perform/ Assist with Procedures:</span>
  <span class="t" style="left:51px;top:1209px">Caregiver has capacity to learn therapeutic regimen:</span>
  <div class="c" style="left:386px;top:1089px"></div><span class="t" style="left:408px;top:1089px">Yes</span><div class="c" style="left:446px;top:1089px"></div><span class="t" style="left:468px;top:1089px">No</span>
  <div class="c" style="left:386px;top:1113px"></div><span class="t" style="left:408px;top:1113px">Yes</span><div class="c" style="left:446px;top:1113px"></div><span class="t" style="left:468px;top:1113px">No</span>
  <div class="c" style="left:386px;top:1137px"></div><span class="t" style="left:408px;top:1137px">Yes</span><div class="c" style="left:446px;top:1137px"></div><span class="t" style="left:468px;top:1137px">No</span>
  <div class="c" style="left:386px;top:1161px"></div><span class="t" style="left:408px;top:1161px">Yes</span><div class="c" style="left:446px;top:1161px"></div><span class="t" style="left:468px;top:1161px">No</span>
  <div class="c" style="left:386px;top:1185px"></div><span class="t" style="left:408px;top:1185px">Yes</span><div class="c" style="left:446px;top:1185px"></div><span class="t" style="left:468px;top:1185px">No</span>
  <div class="c" style="left:386px;top:1209px"></div><span class="t" style="left:408px;top:1209px">Yes</span><div class="c" style="left:446px;top:1209px"></div><span class="t" style="left:468px;top:1209px">No</span>
  <span class="t" style="left:51px;top:1234px">Comments:</span><div class="f" style="left:124px;top:1234px;width:361px"></div>

  <span class="t b u" style="left:51px;top:1275px">Are There Any Signs of Abuse or Neglect from Family or Caregiver?:</span>
  <div class="c" style="left:504px;top:1275px"></div><span class="t b u" style="left:524px;top:1275px">Yes</span>
  <div class="c" style="left:569px;top:1275px"></div><span class="t b u" style="left:590px;top:1275px">No</span>
  <span class="t b u" style="left:51px;top:1299px">If Yes, describe:</span>
  <div class="note-box"></div>
</div>
</body>
</html>
```